300 x 250 Web Ad for Porn Website

300 x 250 web ad that will appear on a porn site. Need to see 3 options, one with each of the 3 girls. Remove the background around the girls.

Underneath the girls image should read in big bold letters: High Speed Internet
Underneath in slightly smaller size: NO Credit Check

To the left of the girl: Save MONEY...

To the right of the girl: So you can buy more PORN

We want it to look very unique, raunchy, and eye catching.

Target Market(s)

Porn website

Industry/Entity Type

Internet Service Provider

Colors

Designer to choose colors to be used in the design.

Requirements
Must have
• Must stand out so people will definitely notice it.
• JPEG and PNG formats

```html
<!DOCTYPE html>
<html lang="en">
<head>
<meta charset="utf-8">
<title>High Speed Internet – Web Ad Set</title>
<link rel="stylesheet" href="https://fonts.googleapis.com/css2?family=Bowlby+One&family=Lilita+One&family=Roboto:ital,wght@1,900&display=swap">
<style>
  :root{
    --page:#ffffff;
    --fire-yellow:#ffd21a;
    --fire-pale:#fff3a0;
    --fire-orange:#f27812;
    --fire-red:#c81e10;
    --deep-red:#6e0c0a;
    --maroon:#3a0505;
    --night-blue:#1a2780;
    --electric-blue:#3566e0;
    --violet:#6a2aa0;
    --bolt:#f4e8ff;
    --text-yellow:#fff04a;
    --text-gold:#f6a300;
    --ink:#0b0b0b;
    --white:#ffffff;
    --photo-dark:#3a1c16;
    --photo-mid:#9a5e48;
    --photo-light:#d9a183;
  }
  *{box-sizing:border-box;margin:0;padding:0}
  html,body{width:1200px;height:1000px;overflow:hidden;background:var(--page)}
  .ad-sheet{position:relative;width:1200px;height:1000px}

  /* ---------- ad base ---------- */
  .ad{
    position:absolute;overflow:hidden;
    background:
      radial-gradient(circle at 82% 12%, var(--fire-pale) 0%, var(--fire-yellow) 14%, transparent 42%),
      radial-gradient(ellipse at 70% 40%, var(--fire-orange) 0%, transparent 60%),
      radial-gradient(circle at 20% 70%, rgba(106,42,160,.55) 0%, transparent 45%),
      radial-gradient(circle at 60% 65%, rgba(255,140,30,.35) 0%, transparent 30%),
      linear-gradient(180deg, var(--fire-orange) 0%, var(--fire-red) 45%, var(--deep-red) 72%, var(--violet) 86%, var(--night-blue) 100%);
  }
  .ad::after{
    content:"";position:absolute;left:0;right:0;bottom:0;height:20%;z-index:0;
    background:linear-gradient(180deg, transparent, rgba(53,102,224,.8) 65%, var(--night-blue));
  }
  .ad__bolts{position:absolute;inset:0;width:100%;height:100%;z-index:1}
  .bolt-glow{fill:none;stroke:var(--violet);stroke-width:6;opacity:.45;vector-effect:non-scaling-stroke}
  .bolt-core{fill:none;stroke:var(--bolt);stroke-width:1.4;vector-effect:non-scaling-stroke}

  .ad__photo{
    position:absolute;z-index:2;top:0;height:100%;
    background:
      radial-gradient(ellipse 60% 55% at 55% 55%, rgba(217,161,131,.75) 0%, rgba(154,94,72,.55) 50%, transparent 85%),
      linear-gradient(90deg, rgba(58,28,22,.85) 0%, rgba(58,28,22,.35) 70%, transparent 100%);
    -webkit-mask-image:linear-gradient(90deg,#000 0%,#000 70%,transparent 100%);
    mask-image:linear-gradient(90deg,#000 0%,#000 70%,transparent 100%);
  }

  /* ---------- tagline ---------- */
  .tagline{position:absolute;z-index:3;text-align:center;line-height:.92;transform:rotate(-5deg)}
  .tagline span{display:block;white-space:nowrap}
  .tagline__save,.tagline__money,.tagline__buy{
    font-family:"Bowlby One", sans-serif;color:var(--maroon);
    -webkit-text-stroke:.07em var(--text-yellow);paint-order:stroke fill;
  }
  .tagline__buy{color:var(--deep-red);-webkit-text-stroke:.05em var(--fire-pale)}
  .tagline__you,.tagline__more{
    font-family:"Roboto", sans-serif;font-style:italic;font-weight:900;
    color:var(--text-yellow);-webkit-text-stroke:.1em var(--ink);paint-order:stroke fill;
  }
  .tagline__porn{font-family:"Bowlby One", sans-serif;color:var(--text-yellow);-webkit-text-stroke:.1em var(--ink);paint-order:stroke fill}
  .tagline .tagline__row{display:block}
  .tagline__row span{display:inline}

  /* ---------- headline & subline ---------- */
  .headline{
    position:absolute;z-index:4;white-space:nowrap;line-height:1;
    font-family:"Lilita One", sans-serif;
    background:linear-gradient(180deg, var(--white) 0%, var(--text-yellow) 45%, var(--text-gold) 100%);
    -webkit-background-clip:text;background-clip:text;-webkit-text-fill-color:transparent;
    filter:drop-shadow(2px 2px 0 var(--ink)) drop-shadow(-1px -1px 0 var(--ink)) drop-shadow(0 0 4px rgba(0,0,0,.8));
    transform:rotate(-4deg) skewX(-8deg);
  }
  .subline{
    position:absolute;z-index:4;white-space:nowrap;
    font-family:"Roboto", sans-serif;font-style:italic;font-weight:900;color:var(--white);
    text-shadow:0 0 4px var(--ink),1px 1px 0 var(--ink);
  }

  /* ---------- 300x250 squares ---------- */
  .ad--square .ad__photo{left:0;width:58%}
  .ad--square .tagline{right:1%;top:3%;width:60%}
  .ad--square .tagline__save{font-size:30px}
  .ad--square .tagline__money{font-size:29px}
  .ad--square .tagline__you{font-size:23px;margin:2px 0}
  .ad--square .tagline__buy{font-size:58px;line-height:.95}
  .ad--square .tagline__more{font-size:16px}
  .ad--square .tagline__porn{font-size:31px}
  .ad--square .headline{left:3%;bottom:16%;font-size:37px}
  .ad--square .subline{right:5%;bottom:4%;font-size:15px}
  .ad--centered .ad__photo{left:12%;width:58%;-webkit-mask-image:linear-gradient(90deg,transparent 0%,#000 20%,#000 70%,transparent 100%);mask-image:linear-gradient(90deg,transparent 0%,#000 20%,#000 70%,transparent 100%)}

  .sq-1{left:31px;top:26px;width:360px;height:300px}
  .sq-2{left:417px;top:26px;width:360px;height:300px}
  .sq-3{left:802px;top:26px;width:360px;height:300px}
  .sq-4{left:226px;top:610px;width:374px;height:360px}
  .sq-5{left:619px;top:610px;width:377px;height:360px}
  .sq-4 .tagline__save,.sq-5 .tagline__save{font-size:34px}
  .sq-4 .tagline__money,.sq-5 .tagline__money{font-size:32px}
  .sq-4 .tagline__you,.sq-5 .tagline__you{font-size:25px}
  .sq-4 .tagline__buy,.sq-5 .tagline__buy{font-size:66px}
  .sq-4 .tagline__porn,.sq-5 .tagline__porn{font-size:35px}
  .sq-4 .tagline__more,.sq-5 .tagline__more{font-size:18px}
  .sq-4 .headline,.sq-5 .headline{font-size:40px;bottom:14%}
  .sq-4 .subline,.sq-5 .subline{font-size:17px}

  /* ---------- banners ---------- */
  .ad--banner .ad__photo{left:0;width:48%}
  .banner-stack{position:absolute;z-index:4;right:5%;top:12%;text-align:center}
  .banner-stack .headline{position:static;display:block;font-size:30px;line-height:1.02}
  .ad--banner .subline{right:6%;bottom:8%;font-size:13px}
  .has-tagline .headline{left:3%;bottom:18%;font-size:35px}
  .banner-tag{position:absolute;z-index:3;right:4%;top:4%;line-height:.9;text-align:right;transform:rotate(-4deg)}
  .banner-tag span{white-space:nowrap}
  .banner-tag .tagline__save,.banner-tag .tagline__money{font-size:14px}
  .banner-tag .tagline__you,.banner-tag .tagline__more{font-size:13px}
  .banner-tag .tagline__buy{font-size:22px}
  .banner-tag .tagline__porn{font-size:16px}
  .bn-1{left:245px;top:342px;width:355px;height:119px}
  .bn-2{left:620px;top:342px;width:355px;height:119px}
  .bn-3{left:245px;top:476px;width:355px;height:119px}
  .bn-4{left:620px;top:476px;width:355px;height:119px}
  .bn-4 .ad__photo{width:55%}
</style>
</head>
<body>
<main class="ad-sheet">

  <section class="ad ad--square sq-1">
    <svg class="ad__bolts" viewBox="0 0 100 100" preserveAspectRatio="none" aria-hidden="true"><polyline class="bolt-glow" points="100,52 86,58 90,62 74,70 78,74 62,84"/><polyline class="bolt-core" points="100,52 86,58 90,62 74,70 78,74 62,84"/><polyline class="bolt-core" points="8,60 14,66 10,70 18,78"/></svg>
    <div class="ad__photo" role="img" aria-label="Model in black lingerie, posed from behind, background removed"></div>
    <div class="tagline"><span class="tagline__save">$ave</span><span class="tagline__money">MONEY...</span><span class="tagline__you">so you can</span><span class="tagline__buy">BUY</span><span class="tagline__row"><span class="tagline__more">more </span><span class="tagline__porn">PORN</span></span></div>
    <p class="headline">High Speed Internet</p>
    <p class="subline">NO Credit Check</p>
  </section>

  <section class="ad ad--square sq-2">
    <svg class="ad__bolts" viewBox="0 0 100 100" preserveAspectRatio="none" aria-hidden="true"><polyline class="bolt-glow" points="100,56 88,60 92,64 76,72 80,76 64,86"/><polyline class="bolt-core" points="100,56 88,60 92,64 76,72 80,76 64,86"/></svg>
    <div class="ad__photo" role="img" aria-label="Model in sheer lace bra, close crop, background removed"></div>
    <div class="tagline"><span class="tagline__save">$ave</span><span class="tagline__money">MONEY...</span><span class="tagline__you">so you can</span><span class="tagline__buy">BUY</span><span class="tagline__row"><span class="tagline__more">more </span><span class="tagline__porn">PORN</span></span></div>
    <p class="headline">High Speed Internet</p>
    <p class="subline">NO Credit Check</p>
  </section>

  <section class="ad ad--square ad--centered sq-3">
    <svg class="ad__bolts" viewBox="0 0 100 100" preserveAspectRatio="none" aria-hidden="true"><polyline class="bolt-glow" points="100,54 88,60 92,64 78,72 82,76 68,86"/><polyline class="bolt-core" points="100,54 88,60 92,64 78,72 82,76 68,86"/></svg>
    <div class="ad__photo" role="img" aria-label="Model in red strappy lingerie with devil horns, background removed"></div>
    <div class="tagline"><span class="tagline__save">$ave</span><span class="tagline__money">MONEY...</span><span class="tagline__you">so you can</span><span class="tagline__buy">BUY</span><span class="tagline__row"><span class="tagline__more">more </span><span class="tagline__porn">PORN</span></span></div>
    <p class="headline">High Speed Internet</p>
    <p class="subline">NO Credit Check</p>
  </section>

  <section class="ad ad--banner bn-1">
    <svg class="ad__bolts" viewBox="0 0 100 100" preserveAspectRatio="none" aria-hidden="true"><polyline class="bolt-glow" points="36,0 48,18 44,24 58,40 54,48 66,62"/><polyline class="bolt-core" points="36,0 48,18 44,24 58,40 54,48 66,62"/></svg>
    <div class="ad__photo" role="img" aria-label="Model in sheer lace bra, background removed"></div>
    <div class="banner-stack"><p class="headline">HIGH SPEED</p><p class="headline">INTERNET</p></div>
    <p class="subline">NO Credit Check</p>
  </section>

  <section class="ad ad--banner has-tagline bn-2">
    <svg class="ad__bolts" viewBox="0 0 100 100" preserveAspectRatio="none" aria-hidden="true"><polyline class="bolt-glow" points="30,0 40,20 36,28 48,44"/><polyline class="bolt-core" points="30,0 40,20 36,28 48,44"/></svg>
    <div class="ad__photo" role="img" aria-label="Model in sheer lace bra, background removed"></div>
    <div class="banner-tag"><span class="tagline__save">$ave</span> <span class="tagline__money">MONEY</span> <span class="tagline__you">so you can</span> <span class="tagline__more">more</span><br><span class="tagline__buy">BUY</span> <span class="tagline__porn">PORN</span></div>
    <p class="headline">High Speed Internet</p>
    <p class="subline">NO Credit Check</p>
  </section>

  <section class="ad ad--banner has-tagline bn-3">
    <svg class="ad__bolts" viewBox="0 0 100 100" preserveAspectRatio="none" aria-hidden="true"><polyline class="bolt-glow" points="100,30 88,36 92,42 80,50"/><polyline class="bolt-core" points="100,30 88,36 92,42 80,50"/></svg>
    <div class="ad__photo" role="img" aria-label="Model in black lingerie from behind, background removed"></div>
    <div class="banner-tag"><span class="tagline__save">$ave</span> <span class="tagline__money">MONEY</span> <span class="tagline__you">so you can</span> <span class="tagline__more">more</span><br><span class="tagline__buy">BUY</span> <span class="tagline__porn">PORN</span></div>
    <p class="headline">High Speed Internet</p>
    <p class="subline">NO Credit Check</p>
  </section>

  <section class="ad ad--banner bn-4">
    <svg class="ad__bolts" viewBox="0 0 100 100" preserveAspectRatio="none" aria-hidden="true"><polyline class="bolt-glow" points="46,0 56,16 52,24 64,38 60,46 72,60"/><polyline class="bolt-core" points="46,0 56,16 52,24 64,38 60,46 72,60"/></svg>
    <div class="ad__photo" role="img" aria-label="Model in black lingerie from behind, close crop, background removed"></div>
    <div class="banner-stack"><p class="headline">HIGH SPEED</p><p class="headline">INTERNET</p></div>
    <p class="subline">NO Credit Check</p>
  </section>

  <section class="ad ad--square sq-4">
    <svg class="ad__bolts" viewBox="0 0 100 100" preserveAspectRatio="none" aria-hidden="true"><polyline class="bolt-glow" points="100,54 88,60 92,64 76,72 80,76 66,86"/><polyline class="bolt-core" points="100,54 88,60 92,64 76,72 80,76 66,86"/></svg>
    <div class="ad__photo" role="img" aria-label="Model in sheer lace bra, background removed"></div>
    <div class="tagline"><span class="tagline__save">$ave</span><span class="tagline__money">MONEY...</span><span class="tagline__you">so you can</span><span class="tagline__buy">BUY</span><span class="tagline__row"><span class="tagline__more">more </span><span class="tagline__porn">PORN</span></span></div>
    <p class="headline">High Speed Internet</p>
    <p class="subline">NO Credit Check</p>
  </section>

  <section class="ad ad--square sq-5">
    <svg class="ad__bolts" viewBox="0 0 100 100" preserveAspectRatio="none" aria-hidden="true"><polyline class="bolt-glow" points="100,50 86,56 90,60 74,68 78,72 62,82"/><polyline class="bolt-core" points="100,50 86,56 90,60 74,68 78,72 62,82"/></svg>
    <div class="ad__photo" role="img" aria-label="Model in black lingerie, posed from behind, background removed"></div>
    <div class="tagline"><span class="tagline__save">$ave</span><span class="tagline__money">MONEY...</span><span class="tagline__you">so you can</span><span class="tagline__buy">BUY</span><span class="tagline__row"><span class="tagline__more">more </span><span class="tagline__porn">PORN</span></span></div>
    <p class="headline">High Speed Internet</p>
    <p class="subline">NO Credit Check</p>
  </section>

</main>
</body>
</html>
```